Brightwave Systems - IT Support Tri-Fold

Need a tri-fold brochure for marketing, pitching managed IT Services. These services include computer/server management, security, cloud backups. The tri-fold should use our logo and colors (Attached)

```html
<!DOCTYPE html>
<html lang="en">
<head>
<meta charset="utf-8">
<title>Brightwave Systems – IT Support Tri-Fold</title>
<link href="https://fonts.googleapis.com/css2?family=Oswald:wght@400;500;600&family=Open+Sans:wght@400;600;700&display=swap" rel="stylesheet">
<style>
:root{
  --navy:#1e2a45;
  --navy-2:#2a3858;
  --red:#d8262d;
  --ink:#2b2f38;
  --muted:#6b7280;
  --line:#dfe3ea;
  --row:#f3f5f8;
  --page:#eef0f3;
  --paper:#ffffff;
}
*{box-sizing:border-box;margin:0;padding:0}
html,body{width:851px;height:1200px;overflow:hidden}
body{background:var(--page);font-family:"Open Sans",Arial,sans-serif;color:var(--ink);position:relative}
.sheet{position:absolute;left:30px;width:791px;height:560px;background:var(--paper);display:grid;grid-template-columns:repeat(3,1fr);box-shadow:0 2px 8px rgba(0,0,0,.18)}
.sheet--outside{top:18px}
.sheet--inside{top:604px}
.panel{position:relative;padding:16px 16px;overflow:hidden;border-right:1px solid var(--line)}
.panel:last-child{border-right:none}
.heading{font-family:"Oswald",Arial,sans-serif;font-weight:400;text-transform:uppercase;font-size:19px;line-height:1.1;letter-spacing:.5px}
.heading--boxed{display:inline-block;background:var(--navy);color:#fff;padding:6px 12px 6px 10px;border-left:4px solid var(--red);margin-left:-16px}
.body-copy{font-size:5.6px;line-height:1.55;color:var(--muted);margin-top:9px}
.body-copy--light{color:#c6cddb}
.photo{display:block;width:100%}
.badges{display:flex;gap:6px;margin-top:10px}
.badge{flex:1;height:20px;background:#e3e7ee;border-radius:2px}

/* testimonial */
.quote-mark{font-family:"Oswald",sans-serif;font-size:34px;color:var(--red);line-height:1;margin-top:8px}
.quote-author{font-size:6px;font-weight:700;color:var(--navy);text-align:center;margin-top:8px}
.quote-role{font-size:5px;color:var(--muted);text-align:center}
.contact-block{position:absolute;left:0;right:0;bottom:0;top:222px;background:var(--navy);color:#fff;padding:16px;text-align:center}
.contact-line{font-size:6px;line-height:1.9;color:#d7dcea}
.btn{display:inline-block;background:var(--red);color:#fff;font-family:"Oswald",sans-serif;font-size:13px;padding:5px 18px;margin:14px 0 10px;letter-spacing:.5px}
.socials{display:flex;justify-content:center;gap:6px}
.socials span{width:12px;height:12px;border-radius:50%;background:#fff;opacity:.85}

/* cover */
.brand{display:flex;align-items:center;gap:8px;margin:6px 0 12px 4px}
.brand-mark{width:22px;height:22px;background:var(--red)}
.brand-name{font-family:"Oswald",sans-serif;font-size:17px;font-weight:500;color:var(--navy)}
.cover-band{background:var(--navy);color:#fff;margin:0 -16px;padding:12px 16px;border-left:6px solid var(--red)}
.cover-band .heading{font-size:22px;font-weight:500}
.cover-sub{font-family:"Oswald",sans-serif;font-size:11px;color:var(--muted);text-transform:uppercase;margin-top:12px;line-height:1.3}
.cover-web{position:absolute;bottom:16px;left:16px;right:16px;text-align:right;font-size:8px;color:var(--navy);font-weight:600}
.cover-web b{color:var(--red)}

/* price tables */
.price-table{width:100%;border-collapse:collapse;margin-top:10px;font-size:5.8px}
.price-table td{padding:3.6px 5px;border-bottom:1px solid var(--line)}
.price-table tr:nth-child(odd) td{background:var(--row)}
.price-table td:last-child{text-align:right;color:var(--red);font-weight:700;width:46px}
.panel--dark{background:var(--navy);color:#fff}
.panel--dark .heading--boxed{background:var(--navy-2)}
.panel--dark .price-table td{border-bottom:1px solid #34426a}
.panel--dark .price-table tr:nth-child(odd) td{background:#25335a}
.panel--dark .price-table tr:nth-child(even) td{background:transparent}
.clients{position:absolute;left:0;right:0;bottom:0;background:var(--navy);padding:8px 12px}
.clients-title{font-family:"Oswald",sans-serif;color:#fff;font-size:9px;margin-bottom:6px}
.client-grid{display:grid;grid-template-columns:repeat(5,1fr);gap:5px}
.client-grid span{height:12px;background:#ffffff;opacity:.9;border-radius:2px}
.call{position:absolute;left:16px;right:16px;bottom:16px;text-align:center}
.call-label{font-family:"Oswald",sans-serif;font-size:18px;color:var(--navy)}
.call-number{display:inline-flex;align-items:center;gap:6px;font-family:"Oswald",sans-serif;font-size:15px;color:#fff;background:var(--red);padding:3px 12px;border-radius:14px;margin-top:4px}
</style>
</head>
<body>

<!-- outside spread -->
<section class="sheet sheet--outside">
  <div class="panel">
    <h2 class="heading heading--boxed">Why People<br>Choose Us</h2>
    <p class="body-copy">For over a decade our team has helped families and small firms keep their computers fast, safe and working. We answer quickly, explain clearly and fix problems the first time, so you can get back to what matters most.</p>
    <p class="body-copy">Our certified technicians handle everything from a single laptop to a full office network. We monitor systems around the clock, patch weak spots before trouble starts and keep your files backed up to secure cloud storage every single day.</p>
    <svg class="photo" style="margin-top:12px" width="232" height="200" role="img" aria-label="Company service van parked outside">
      <defs><linearGradient id="vanGrad" x1="0" y1="0" x2="0" y2="1"><stop offset="0" stop-color="#c9d3df"/><stop offset="1" stop-color="#8e99a8"/></linearGradient></defs>
      <rect width="232" height="200" fill="url(#vanGrad)"/>
    </svg>
    <div class="badges"><span class="badge"></span><span class="badge"></span><span class="badge"></span><span class="badge"></span></div>
    <p class="body-copy">Trusted partner listings and industry certifications.</p>
  </div>

  <div class="panel">
    <h2 class="heading" style="color:var(--navy)">What<br>Customers Say</h2>
    <div class="quote-mark">“</div>
    <p class="body-copy" style="margin-top:0">Our office lost a server on a Monday morning and their team had us running again before lunch. Since then they manage all our machines and we have not had a single day of downtime. Friendly, fast and honest.</p>
    <p class="quote-author">Laura Bennett</p>
    <p class="quote-role">Office Manager, Harbor Dental</p>
    <div class="contact-block">
      <p class="contact-line">118 Lakeview Drive, Riverton, ST 00000</p>
      <p class="contact-line">+1 555-018-2740</p>
      <p class="contact-line">help@brightwave.systems</p>
      <p class="contact-line">www.brightwave.systems</p>
      <span class="btn">GET IN TOUCH</span>
      <div class="socials"><span></span><span></span><span></span><span></span></div>
    </div>
  </div>

  <div class="panel">
    <div class="brand"><span class="brand-mark"></span><span class="brand-name">Brightwave Systems</span></div>
    <svg class="photo" width="232" height="230" role="img" aria-label="Two technicians working beside a server rack">
      <defs><linearGradient id="srvGrad" x1="0" y1="0" x2="1" y2="1"><stop offset="0" stop-color="#5c6d85"/><stop offset="1" stop-color="#1f2b40"/></linearGradient></defs>
      <rect width="232" height="230" fill="url(#srvGrad)"/>
    </svg>
    <div class="cover-band"><h1 class="heading">Home and Business<br>IT Services</h1></div>
    <p class="cover-sub">Software Service<br>Web Solution</p>
    <p class="cover-web">www.<b>brightwave</b>.systems</p>
  </div>
</section>

<!-- inside spread -->
<section class="sheet sheet--inside">
  <div class="panel">
    <h2 class="heading heading--boxed">Residential<br>Services</h2>
    <p class="body-copy">From slow laptops to home networks, our technicians come to you and fix it right. Clear flat prices, no hidden fees.</p>
    <table class="price-table">
      <tr><td>Wired/Wireless Network Install &amp; Setup</td><td>$89/hr</td></tr>
      <tr><td>Tune Up</td><td>$59/hr</td></tr>
      <tr><td>Virus Removal</td><td>$79/hr</td></tr>
      <tr><td>Hardware Install</td><td>$69/hr</td></tr>
      <tr><td>Phone Setup &amp; Configuration</td><td>$49/hr</td></tr>
      <tr><td>Home Entertainment Set</td><td>$89/hr</td></tr>
      <tr><td>TV &amp; Display Install &amp; Mounting</td><td>$99/hr</td></tr>
      <tr><td>Onsite Troubleshooting</td><td>$79/hr</td></tr>
      <tr><td>Printer Setup</td><td>$49/hr</td></tr>
      <tr><td>Data Backup</td><td>$69/hr</td></tr>
      <tr><td>Computer Setup</td><td>$69/hr</td></tr>
      <tr><td>Software Install</td><td>$49/hr</td></tr>
      <tr><td>Data Recovery</td><td>$99/hr</td></tr>
    </table>
    <div class="clients">
      <p class="clients-title">Our Clients</p>
      <div class="client-grid"><span></span><span></span><span></span><span></span><span></span><span></span><span></span><span></span><span></span><span></span></div>
    </div>
  </div>

  <div class="panel panel--dark">
    <h2 class="heading heading--boxed">Business<br>Services</h2>
    <p class="body-copy body-copy--light">Managed IT for growing teams: server care, security, cloud backups and help desk support under one monthly plan, so your staff stays productive.</p>
    <table class="price-table">
      <tr><td>Email Setup (Business)</td><td>$99/hr</td></tr>
      <tr><td>Virus Removal (Business)</td><td>$99/hr</td></tr>
      <tr><td>Hardware Install (Business)</td><td>$89/hr</td></tr>
      <tr><td>Computer Setup (Business)</td><td>$89/hr</td></tr>
      <tr><td>Printer Setup (Business)</td><td>$69/hr</td></tr>
      <tr><td>Data Backup (Business)</td><td>$99/hr</td></tr>
      <tr><td>Data Recovery (Business)</td><td>$129/hr</td></tr>
      <tr><td>Server Setup &amp; Monitoring</td><td>$149/hr</td></tr>
      <tr><td>Network Security Audit</td><td>$139/hr</td></tr>
      <tr><td>Firewall Configuration</td><td>$119/hr</td></tr>
      <tr><td>Cloud Migration</td><td>$129/hr</td></tr>
      <tr><td>Software Licensing</td><td>$79/hr</td></tr>
      <tr><td>Managed Help Desk</td><td>$99/hr</td></tr>
      <tr><td>Remote Support</td><td>$69/hr</td></tr>
      <tr><td>Graphic Design</td><td>$79/hr</td></tr>
      <tr><td>Server Configuration</td><td>$139/hr</td></tr>
      <tr><td>VoIP Phone Systems</td><td>$99/hr</td></tr>
      <tr><td>Office Setup</td><td>$109/hr</td></tr>
    </table>
  </div>

  <div class="panel">
    <h2 class="heading heading--boxed">Web<br>Services</h2>
    <p class="body-copy">We build fast, secure websites that look great on every screen. Our designers and developers handle hosting, domains, updates and search visibility so your business is easy to find online.</p>
    <p class="body-copy">Every site comes with daily backups, security monitoring and friendly support from a local team that knows your goals and answers the phone.</p>
    <svg class="photo" style="margin-top:14px" width="232" height="230" role="img" aria-label="Website shown on laptop, tablet and phone screens">
      <defs><linearGradient id="webGrad" x1="0" y1="0" x2="1" y2="1"><stop offset="0" stop-color="#eef1f6"/><stop offset="1" stop-color="#b8c3d3"/></linearGradient></defs>
      <rect width="232" height="230" fill="url(#webGrad)"/>
    </svg>
    <div class="call">
      <p class="call-label">CALL US NOW</p>
      <span class="call-number">
        <svg width="11" height="11" viewBox="0 0 24 24"><path fill="#fff" d="M6.6 10.8a15.1 15.1 0 0 0 6.6 6.6l2.2-2.2c.3-.3.7-.4 1-.2 1.1.4 2.3.6 3.6.6.6 0 1 .4 1 1V20c0 .6-.4 1-1 1A17 17 0 0 1 3 4c0-.6.4-1 1-1h3.5c.6 0 1 .4 1 1 0 1.3.2 2.5.6 3.6.1.3 0 .7-.2 1z"/></svg>
        +1 555-018-2740
      </span>
    </div>
  </div>
</section>

</body>
</html>
```